Property management company looking for modern card design

We at Blue Maple Holdings provides property management services for its residential and commercial properties, with expertise in all categories of multifamily, industrial and office projects throughout California.

We need a business card design that is professional and modern designed business card. In our field, clients get hundreds of business cards, we would like our card to stand out.

Please avoid small print.

Target Market(s)

Professionals and high end clients

Industry/Entity Type

Financial Planning

Contact Information for Business Card

Company Name: Blue Maple Holdings, Name, email, license #, phone number, website bluemapleholdings.example

Font styles to use
Sans Serif

Requirements
Must have
• The card design needs to be adaptable because there is a possibly we will be expanding into different sectors other than real estate. The card design should be focused on financial planning and asset management.
Nice to have
• Modern and simple business card. Eye catching. Non-standard size/shaped cards would be great.
• bluemapleholdings.example
Should not have
• Too many bright color or any pictures or shapes of real estate stuff.

```html
<!DOCTYPE html>
<html lang="en">
<head>
<meta charset="UTF-8">
<title>Blue Maple Holdings – Business Card</title>
<link href="https://fonts.googleapis.com/css2?family=Open+Sans:wght@400;600;700&display=swap" rel="stylesheet">
<style>
  :root {
    --accent: #d8263c;
    --ink: #1f1f21;
    --ink-soft: #8a8a8e;
    --url-ink: #555559;
    --paper: #ffffff;
    --card-dark: #3b3b3e;
    --card-darker: #2a2a2c;
    --back-url: #cfcfd2;
    --backdrop: #e6e6e8;
  }
  * { box-sizing: border-box; margin: 0; padding: 0; }
  html, body {
    width: 1200px; height: 1000px; overflow: hidden;
    background: var(--backdrop);
    font-family: "Open Sans", Arial, sans-serif;
  }
  .stage { position: relative; width: 1200px; height: 1000px; }
  .card {
    position: absolute; top: 130px;
    width: 420px; height: 740px;
    border-radius: 4px;
    box-shadow: 0 18px 40px rgba(0,0,0,.18);
    overflow: hidden;
  }
  /* Front */
  .card--front { left: 150px; background: var(--paper); }
  .brand {
    position: absolute; top: 225px; left: 0; right: 0;
    text-align: center;
  }
  .brand__name {
    color: var(--accent); font-weight: 600;
    font-size: 31px; letter-spacing: 1px; line-height: 1.2;
  }
  .brand__url {
    margin-top: 6px; color: var(--url-ink); font-weight: 700; font-size: 16px;
  }
  .tab {
    position: absolute; left: 0; top: 430px;
    width: 150px; height: 110px;
    background: var(--accent);
    border-radius: 0 55px 55px 0;
  }
  .person { position: absolute; left: 170px; top: 442px; }
  .person__name {
    font-size: 27px; font-weight: 700; letter-spacing: 2px; color: var(--ink);
  }
  .person__role { font-size: 20px; color: var(--accent); margin-top: 2px; }
  .contacts {
    position: absolute; left: 48px; top: 580px;
    list-style: none;
  }
  .contacts li {
    display: flex; align-items: center; gap: 22px;
    font-size: 16.5px; line-height: 26px; color: var(--ink-soft);
    margin-bottom: 5px;
  }
  .contacts svg { width: 18px; height: 18px; flex: none; }
  /* Back */
  .card--back {
    left: 630px;
    background: linear-gradient(160deg, var(--card-dark) 0%, var(--card-darker) 100%);
  }
  .back-band {
    position: absolute; right: 0; top: 330px;
    width: 360px; height: 92px;
    background: var(--accent);
    border-radius: 46px 0 0 46px;
    display: flex; align-items: center; padding-left: 30px;
    color: #fff; font-weight: 600; font-size: 29px;
  }
  .back-url {
    position: absolute; right: 24px; top: 436px;
    color: var(--back-url); font-size: 17px; font-weight: 600;
  }
</style>
</head>
<body>
<main class="stage">
  <section class="card card--front">
    <div class="brand">
      <div class="brand__name">Blue Maple Holdings</div>
      <div class="brand__url">www.bluemapleholdings.example</div>
    </div>
    <div class="tab"></div>
    <div class="person">
      <div class="person__name">DANIEL REYES</div>
      <div class="person__role">Marketing Head</div>
    </div>
    <ul class="contacts">
      <li>
        <svg viewBox="0 0 24 24" fill="none" stroke="#8a8a8e" stroke-width="1.6"><path d="M5 3h4l2 5-2.5 1.5a11 11 0 0 0 6 6L16 13l5 2v4a2 2 0 0 1-2 2A16 16 0 0 1 3 5a2 2 0 0 1 2-2z"/></svg>
        +000 55501 2468
      </li>
      <li>
        <svg viewBox="0 0 24 24" fill="none" stroke="#8a8a8e" stroke-width="1.6"><rect x="3" y="5" width="18" height="14" rx="1"/><path d="M3 6l9 7 9-7"/></svg>
        dan@bluemapleholdings.example
      </li>
      <li>
        <svg viewBox="0 0 24 24" fill="none" stroke="#8a8a8e" stroke-width="1.6"><circle cx="12" cy="12" r="9"/><path d="M3 12h18M12 3c3 3 3 15 0 18M12 3c-3 3-3 15 0 18"/></svg>
        bluemapleholdings.example
      </li>
      <li>
        <svg viewBox="0 0 24 24" fill="none" stroke="#8a8a8e" stroke-width="1.6"><path d="M12 22s7-7 7-12a7 7 0 0 0-14 0c0 5 7 12 7 12z"/><circle cx="12" cy="10" r="2.5"/></svg>
        Your Street Address<br>New York, 1234
      </li>
    </ul>
  </section>

  <section class="card card--back">
    <div class="back-band">Blue Maple Holdings</div>
    <div class="back-url">bluemapleholdings.example</div>
  </section>
</main>
</body>
</html>
```